Garden of Eden - Digital Party Invite

I'm throwing a Halloween party with the theme "Garden of Eden". The invite will be sent via Tidewell Cards. I need a custom design for the invite. Here are the details:
The image needs to be 670x970.
Needs to be sexy - maybe with Adam & Eve, and the snake w/the apple, etc
Text should be:
You Are Invited To
The Garden of Eden
Sat Oct 26 7:00PM
at
Dinah & Tobias's Home
612 North Birch Rd 7B
Costumes Highly Encouraged
Adults Only Please

```html
<!DOCTYPE html>
<html lang="en">
<head>
<meta charset="utf-8">
<title>The Garden of Eden – Party Invitation</title>
<link rel="stylesheet" href="https://fonts.googleapis.com/css2?family=Tinos:wght@700&family=Montserrat:wght@400;600&display=swap">
<style>
  :root {
    --backdrop: #d9d9d7;
    --paper: #f6f1ea;
    --rose: #e6588f;
    --gold: #cfae6e;
    --floral-peach: #f3c9a0;
    --floral-yellow: #f2d774;
    --floral-green: #b9d9a0;
    --floral-blue: #a9cde0;
    --floral-pink: #eab4c8;
    --floral-plum: #b590a8;
    --scene-green: #6f9c58;
    --scene-sky: #bfd9d4;
    --scene-earth: #c9b98a;
  }
  * { margin: 0; padding: 0; box-sizing: border-box; }
  html, body {
    width: 1200px;
    height: 1200px;
    overflow: hidden;
    background: var(--backdrop);
  }
  .invite {
    position: absolute;
    left: 205px;
    top: 40px;
    width: 790px;
    height: 1120px;
    background: var(--paper);
    box-shadow: 0 6px 24px rgba(0,0,0,0.18);
    overflow: hidden;
  }
  .floral-border {
    position: absolute;
    inset: 0;
    background:
      radial-gradient(circle at 12% 10%, var(--floral-peach) 0, transparent 22%),
      radial-gradient(circle at 50% 5%, var(--floral-peach) 0, transparent 18%),
      radial-gradient(circle at 90% 10%, var(--floral-blue) 0, transparent 20%),
      radial-gradient(circle at 6% 45%, var(--floral-yellow) 0, transparent 22%),
      radial-gradient(circle at 96% 45%, var(--floral-plum) 0, transparent 20%),
      radial-gradient(circle at 94% 72%, var(--floral-yellow) 0, transparent 18%),
      radial-gradient(circle at 6% 80%, var(--floral-green) 0, transparent 22%),
      radial-gradient(circle at 22% 96%, var(--floral-pink) 0, transparent 18%),
      radial-gradient(circle at 72% 92%, var(--floral-green) 0, transparent 20%),
      radial-gradient(circle at 92% 96%, var(--floral-yellow) 0, transparent 16%),
      var(--paper);
  }
  .inner-panel {
    position: absolute;
    left: 114px;
    top: 119px;
    width: 553px;
    height: 883px;
    background: var(--paper);
    border: 2px solid var(--gold);
  }
  .garden-scene {
    position: absolute;
    left: 240px;
    top: 236px;
    width: 308px;
    height: 213px;
    background: linear-gradient(180deg, var(--scene-green) 0%, var(--scene-green) 35%, var(--scene-sky) 55%, var(--scene-earth) 78%, var(--scene-green) 100%);
  }
  .invite-text {
    position: absolute;
    left: 0;
    width: 100%;
    text-align: center;
    color: var(--rose);
    font-family: "Montserrat", sans-serif;
    line-height: 1;
    white-space: nowrap;
  }
  .lead { top: 474px; font-size: 22px; letter-spacing: 1px; font-weight: 400; }
  .title {
    font-family: "Tinos", serif;
    font-weight: 700;
    font-size: 63px;
    letter-spacing: 1px;
  }
  .title-line-1 { top: 508px; }
  .title-line-2 { top: 583px; }
  .date { top: 684px; font-size: 23px; font-weight: 600; letter-spacing: 0.5px; }
  .connector { top: 713px; font-size: 22px; font-weight: 400; }
  .hosts { top: 741px; font-size: 24px; font-weight: 600; letter-spacing: 0.5px; }
  .address { top: 770px; font-size: 24px; font-weight: 400; letter-spacing: 0.5px; }
  .note-costume { top: 839px; font-size: 18px; font-weight: 600; letter-spacing: 0.5px; }
  .note-adults { top: 862px; font-size: 18px; font-weight: 400; letter-spacing: 0.8px; }
</style>
</head>
<body>
  <main class="invite">
    <div class="floral-border" role="img" aria-label="Watercolour floral border of peach, yellow, blue, green and pink blossoms"></div>
    <div class="inner-panel"></div>
    <div class="garden-scene" role="img" aria-label="Painted garden scene with two figures beneath a fruit tree and a serpent coiled around the trunk"></div>

    <p class="invite-text lead">YOU ARE INVITED TO</p>
    <h1 class="invite-text title title-line-1">THE GARDEN</h1>
    <h1 class="invite-text title title-line-2">OF EDEN</h1>
    <p class="invite-text date">SAT OCT 26 7:00PM</p>
    <p class="invite-text connector">at</p>
    <p class="invite-text hosts">DINAH &amp; TOBIAS'S HOME</p>
    <p class="invite-text address">612 North Birch Rd 7B</p>
    <p class="invite-text note-costume">COSTUMES HIGHLY ENCOURAGED</p>
    <p class="invite-text note-adults">ADULTS ONLY PLEASE</p>
  </main>
</body>
</html>
```